Brimwell Baits Website

Brimwell Baits is a start-up fishing lure company, specializing in offshore saltwater fishing lures that dive deep into the water to attract large game fish (wahoo, king mackerel, tuna, cobia, dorado).

The target market is primarily affluent outdoorsman and woman that appreciate high quality fishing equipment and spend a significant amount of time and money in their pursuits of large game fish. I would classify offshore fishing of this type as an "extreme sport", so action and boldness are good color and graphic themes for a website like this.

I have several websites in this industry that I like and would be directed at similar customers:
http://www.tarnquistgear.example/
http://www.moxvane.example/moxvane-lures/
http://www.gullridgemarine.example/
http://www.brinkhaul.example/

The tag line for the company is "Go Deep". I have attached the company logo in .eps format.

Navigation Menu
Home | Company | Products | What is QV-snapline? | Tackle Shop | Contact Us | Media | Distributors

Scope: Landing page design & secondary page templates.
Updates

I don't have product images yet, as they are in manufacturing. I am more interested in creating a brand image, then I can add product images later and incorporate those into the page.

Target Market(s)

Affluent offshore sportsman
Distributors of fishing lures: RodHaven
Retailers of fishing lures: FinCove, Dortmiers

Industry/Entity Type

Font styles to use
Serif
Sans Serif

Requirements
Must have
• Company Logo
QV-snapline Logo incorporated into design - QV-snapline is the key unique identifier of the lure built into the front diving lip in the image below. In addition to the company logo, this logo should be prominent on the landing page. I uploaded multiple colors to accommodate several different color selections on the landing page.

```html
<!DOCTYPE html>
<html lang="en">
<head>
<meta charset="utf-8">
<title>Brimwell Baits – Products</title>
<link href="https://fonts.googleapis.com/css2?family=Marcellus&family=Crimson+Text&family=Arimo:wght@400;700&display=swap" rel="stylesheet">
<style>
  :root {
    --page-bg: #e1e2e6;
    --nav-bg: #abc7d7;
    --navy: #0c2d3e;
    --footer-bg: #0c3549;
    --bottom-bg: #000000;
    --orange: #f07a26;
    --text-grey: #555a60;
    --button-blue: #3aa3d8;
    --button-blue-light: #5fc0ec;
    --button-dark: #4a4d52;
    --arrow-grey: #c8c9cd;
    --link-cyan: #29a9e0;
    --white: #ffffff;
  }
  * { box-sizing: border-box; margin: 0; padding: 0; }
  html, body { width: 921px; height: 1200px; overflow: hidden; }
  body { position: relative; background: var(--page-bg); font-family: "Arimo", Arial, sans-serif; }

  .brand {
    position: absolute; left: 385px; top: 52px; width: 265px; height: 60px;
    display: flex; align-items: center; justify-content: center; gap: 12px;
  }
  .brand-dot { width: 26px; height: 26px; border-radius: 50%; background: var(--orange); }
  .brand-name { font-family: "Marcellus", serif; font-size: 32px; color: var(--navy); white-space: nowrap; }

  .main-nav {
    position: absolute; left: 68px; top: 162px; width: 789px; height: 44px;
    background: var(--nav-bg); display: flex; align-items: stretch;
  }
  .main-nav a {
    font-family: "Marcellus", serif; font-size: 13px; color: var(--navy);
    text-decoration: none; display: flex; align-items: center; padding: 0 10px;
  }
  .main-nav a:first-child { padding-left: 20px; padding-right: 26px; }
  .main-nav a.is-active { background: var(--navy); color: var(--white); }

  .page-title {
    position: absolute; left: 85px; top: 285px;
    font-family: "Marcellus", serif; font-weight: 400; font-size: 64px; color: var(--orange);
    text-shadow: 0 0 8px rgba(255,255,255,0.9), 0 0 3px rgba(255,255,255,0.9);
  }

  .carousel-arrow {
    position: absolute; top: 480px; width: 32px; height: 66px;
    background: var(--arrow-grey); border-radius: 3px;
    display: flex; align-items: center; justify-content: center;
  }
  .carousel-arrow.prev { left: 67px; }
  .carousel-arrow.next { left: 822px; }

  .product-photo { position: absolute; }
  .photo-pack { left: 107px; top: 450px; width: 245px; height: 150px; background: linear-gradient(135deg, #58b6e2, #c7e84b 55%, #8a62c8); border-radius: 4px; }
  .photo-squid { left: 418px; top: 356px; width: 110px; height: 254px; background: linear-gradient(180deg, #79c3ec, #8a2a9e 50%, #e8356e); border-radius: 40px 40px 20px 20px; }
  .photo-skirt { left: 650px; top: 360px; width: 80px; height: 260px; background: linear-gradient(180deg, #d9dadb 0 25%, #1d2b3a 35%, #2677b8 70%, #1f3f5a); border-radius: 30px 30px 10px 10px; }

  .product-card { position: absolute; top: 660px; width: 195px; }
  .product-card p { font-family: "Crimson Text", serif; font-size: 13px; line-height: 17px; color: var(--text-grey); }
  .read-more {
    margin-top: 23px; display: flex; width: 113px; height: 23px; border-radius: 3px; overflow: hidden;
    box-shadow: 0 1px 2px rgba(0,0,0,0.35);
  }
  .read-more .icon { width: 26px; background: var(--button-dark); display: flex; align-items: center; justify-content: center; }
  .read-more .label {
    flex: 1; background: linear-gradient(180deg, var(--button-blue-light), var(--button-blue));
    color: var(--white); font-size: 9.5px; display: flex; align-items: center; justify-content: center;
  }

  .section-divider {
    position: absolute; left: 170px; top: 789px; width: 590px; height: 3px;
    background: radial-gradient(ellipse at center, rgba(120,122,128,0.7), rgba(120,122,128,0) 70%);
  }

  .site-footer { position: absolute; left: 0; top: 843px; width: 921px; height: 277px; background: var(--footer-bg); color: var(--white); }
  .footer-heading { position: absolute; font-family: "Marcellus", serif; font-weight: 400; font-size: 22px; }
  .footer-rule { position: absolute; height: 1px; background: linear-gradient(90deg, var(--orange), rgba(240,122,38,0)); }
  .quick-links { position: absolute; left: 66px; top: 61px; list-style: none; }
  .quick-links li { font-size: 9.5px; font-weight: 700; height: 21.7px; }
  .world-map { position: absolute; left: 235px; top: 62px; width: 166px; height: 120px; background: radial-gradient(ellipse at center, rgba(190,205,215,0.55), rgba(190,205,215,0.1) 70%); border-radius: 6px; }
  .contact-details { position: absolute; left: 423px; top: 67px; font-size: 9px; font-weight: 700; line-height: 13px; }
  .contact-details p { margin-bottom: 12px; }
  .contact-form label { position: absolute; left: 618px; font-size: 12px; }
  .contact-form .field { position: absolute; left: 678px; width: 182px; background: var(--white); border-radius: 3px; box-shadow: inset 0 1px 2px rgba(0,0,0,0.25); }
  .submit-btn { position: absolute; left: 678px; top: 235px; width: 63px; height: 24px; background: linear-gradient(180deg, #fff, #e3e3e3); border-radius: 3px; color: var(--navy); font-size: 11px; display: flex; align-items: center; justify-content: center; }

  .bottom-bar { position: absolute; left: 0; top: 1120px; width: 921px; height: 80px; background: var(--bottom-bg); color: var(--white); }
  .copyright { position: absolute; left: 63px; top: 45px; font-size: 11.5px; }
  .copyright span { color: var(--link-cyan); }
  .follow-label { position: absolute; left: 667px; top: 15px; font-size: 11px; }
  .social-list { position: absolute; left: 666px; top: 33px; display: flex; gap: 5px; }
  .social-list li { list-style: none; width: 24px; height: 24px; border-radius: 4px; background: #c9ccd1; }
</style>
</head>
<body>

<header>
  <div class="brand"><span class="brand-dot"></span><span class="brand-name">Brimwell Baits</span></div>
  <nav class="main-nav">
    <a href="#">HOME</a>
    <a href="#">COMPANY</a>
    <a href="#" class="is-active">PRODUCTS</a>
    <a href="#">WHAT IS QV-SNAPLINE?</a>
    <a href="#">TACKLESHOP</a>
    <a href="#">CONTACT US</a>
    <a href="#">MEDIA</a>
    <a href="#">DISTRIBUTORS</a>
  </nav>
</header>

<main>
  <h1 class="page-title">Products</h1>

  <div class="carousel-arrow prev"><svg width="14" height="20" viewBox="0 0 14 20"><path d="M11 2 L3 10 L11 18" fill="none" stroke="#fff" stroke-width="3"/></svg></div>
  <div class="carousel-arrow next"><svg width="14" height="20" viewBox="0 0 14 20"><path d="M3 2 L11 10 L3 18" fill="none" stroke="#fff" stroke-width="3"/></svg></div>

  <div class="product-photo photo-pack" role="img" aria-label="Pack of trolling lures with purple heads and chartreuse skirts"></div>
  <div class="product-photo photo-squid" role="img" aria-label="Translucent blue and purple squid lure"></div>
  <div class="product-photo photo-skirt" role="img" aria-label="Rigged blue and black skirted trolling lure with hook"></div>

  <article class="product-card" style="left:117px">
    <p>Lorem Ipsum is simply dummy text of the printing and typesetting industry.</p>
    <a class="read-more" href="#"><span class="icon"><svg width="12" height="8" viewBox="0 0 12 8"><path d="M0 3h7V0l5 4-5 4V5H0z" fill="#fff"/></svg></span><span class="label">READ MORE</span></a>
  </article>
  <article class="product-card" style="left:368px">
    <p>Lorem Ipsum is simply dummy text of the printing and typesetting industry.</p>
    <a class="read-more" href="#"><span class="icon"><svg width="12" height="8" viewBox="0 0 12 8"><path d="M0 3h7V0l5 4-5 4V5H0z" fill="#fff"/></svg></span><span class="label">READ MORE</span></a>
  </article>
  <article class="product-card" style="left:620px">
    <p>Lorem Ipsum is simply dummy text of the printing and typesetting industry.</p>
    <a class="read-more" href="#"><span class="icon"><svg width="12" height="8" viewBox="0 0 12 8"><path d="M0 3h7V0l5 4-5 4V5H0z" fill="#fff"/></svg></span><span class="label">READ MORE</span></a>
  </article>

  <div class="section-divider"></div>
</main>

<footer class="site-footer">
  <h2 class="footer-heading" style="left:67px;top:16px">Quick Links</h2>
  <div class="footer-rule" style="left:67px;top:48px;width:160px"></div>
  <ul class="quick-links">
    <li>HOME</li><li>COMPANY</li><li>PRODUCTS</li><li>WHAT'S QV-SNAPLINE?</li>
    <li>TACKLE SHOP</li><li>CONTACT US</li><li>MEDIA</li><li>DISTRIBUTORS</li>
  </ul>

  <h2 class="footer-heading" style="left:236px;top:17px">Contact Us</h2>
  <div class="footer-rule" style="left:236px;top:48px;width:365px"></div>
  <div class="world-map" role="img" aria-label="Dotted world map"></div>
  <div class="contact-details">
    <p>Local Street Address,<br>Country, City, Zipcode</p>
    <p>Tel : (+000) 000 0000<br>Fax : (+000) 000 0000</p>
    <p>E-mail : info@brimwellbaits.example<br>Website : http://www.brimwellbaits.example</p>
  </div>

  <h2 class="footer-heading" style="left:618px;top:17px">Get in touch</h2>
  <div class="footer-rule" style="left:618px;top:48px;width:100px"></div>
  <div class="footer-rule" style="left:728px;top:48px;width:155px"></div>
  <form class="contact-form">
    <label style="top:67px">Name</label>
    <div class="field" style="top:62px;height:24px"></div>
    <label style="top:99px">E-mail</label>
    <div class="field" style="top:94px;height:24px"></div>
    <label style="top:132px">Message</label>
    <div class="field" style="top:127px;height:100px"></div>
    <div class="submit-btn">SUBMIT</div>
  </form>
</footer>

<div class="bottom-bar">
  <p class="copyright">Copyright © 2015 <span>Brimwell Baits</span></p>
  <p class="follow-label">Follow Us On :</p>
  <ul class="social-list" aria-label="Social links">
    <li></li><li></li><li></li><li></li><li></li><li></li><li></li>
  </ul>
</div>

</body>
</html>
```